Simple but strong message business card.

I will be using this to communicate a message about how we are different from our main competitor. I will be giving these out at a trade show. It needs to have our logo and then communicate that we do not charge PCI Fees. Our competitor charges junk fees at an exorbitant amount and our target audience is aware of it and tired of the BS.

Target Market(s)

Attendees of a trade show. General managers of the ridgeline growers union. www.fieldhallmark.net

Contact Information for Business Card

Font styles to use
Sans Serif

Colors

Designer to choose colors to be used in the design.

Requirements
Must have
• Our logo. and the message of No PCI Fees
• contact email - tbrolin@quillmerchant.net
• contact name - Dane Brolin
• contact phone - 303-555-0142

```html
<!DOCTYPE html>
<html lang="en">
<head>
<meta charset="utf-8">
<title>Quill Merchant Services – Business Card</title>
<link rel="stylesheet" href="https://fonts.googleapis.com/css2?family=Open+Sans:wght@600&family=Arimo:wght@400;700&display=swap">
<style>
  :root {
    --bg: #c9c9c9;
    --card: #f1f1f1;
    --card-edge: #e4e4e4;
    --green: #6cb33f;
    --green-soft: rgba(108, 179, 63, 0.28);
    --grey: #6f7378;
    --grey-dark: #55595e;
  }
  * { margin: 0; padding: 0; box-sizing: border-box; }
  html, body { width: 1200px; height: 900px; overflow: hidden; }
  body {
    background: var(--bg);
    font-family: "Arimo", Arial, sans-serif;
    position: relative;
  }
  .card {
    position: absolute;
    left: 290px;
    width: 620px;
    height: 344px;
    border-radius: 22px;
    background: linear-gradient(100deg, var(--card-edge) 0%, var(--card) 60%, #f7f7f7 100%);
    overflow: hidden;
  }
  .card--front { top: 88px; }
  .card--back { top: 470px; }
  .particle-art {
    position: absolute;
    right: 0;
    top: 0;
    width: 250px;
    height: 100%;
    background: radial-gradient(ellipse at 90% 50%, var(--green-soft) 0%, rgba(108,179,63,0.12) 45%, rgba(108,179,63,0) 75%);
  }
  .wordmark {
    position: absolute;
    display: flex;
    align-items: center;
    gap: 12px;
    font-family: "Open Sans", Arial, sans-serif;
    font-weight: 600;
    color: var(--green);
    line-height: 1.05;
  }
  .wordmark__dot {
    flex: none;
    border-radius: 50%;
    background: var(--green);
  }
  .card--front .wordmark { left: 42px; top: 78px; font-size: 27px; }
  .card--front .wordmark__dot { width: 38px; height: 38px; }
  .contact { position: absolute; left: 52px; top: 206px; }
  .contact__name { color: var(--green); font-weight: 700; font-size: 17px; letter-spacing: 0.3px; }
  .contact__title { color: var(--grey); font-size: 13.5px; letter-spacing: 0.6px; margin-top: 2px; }
  .contact__lines { margin-top: 14px; color: var(--green); font-size: 15px; line-height: 1.5; }
  .card--back .wordmark {
    left: 0; right: 0; top: 108px;
    justify-content: center;
    font-size: 33px;
  }
  .card--back .wordmark__dot { width: 46px; height: 46px; }
  .tagline-rule {
    position: absolute;
    left: 300px; top: 213px;
    width: 17px; height: 2px;
    background: var(--green);
  }
  .tagline {
    position: absolute;
    left: 0; right: 0; top: 230px;
    text-align: center;
    font-size: 17px;
    color: var(--green);
  }
  .tagline strong { color: var(--grey-dark); font-weight: 400; }
</style>
</head>
<body>
  <section class="card card--front">
    <div class="particle-art" role="img" aria-label="Fine green dotted particle pattern fading in from the right edge"></div>
    <div class="wordmark">
      <span class="wordmark__dot"></span>
      <span>Quill Merchant<br>Services</span>
    </div>
    <div class="contact">
      <p class="contact__name">DANE BROLIN</p>
      <p class="contact__title">MANAGING DIRECTOR</p>
      <div class="contact__lines">
        <p>303-555-0142</p>
        <p>tbrolin@quillmerchant.net</p>
        <p>www.quillmerchant.net</p>
      </div>
    </div>
  </section>

  <section class="card card--back">
    <div class="particle-art" role="img" aria-label="Fine green dotted particle pattern fading in from the right edge"></div>
    <div class="wordmark">
      <span class="wordmark__dot"></span>
      <span>Quill Merchant<br>Services</span>
    </div>
    <div class="tagline-rule"></div>
    <p class="tagline">No <strong>PCI</strong> Fees</p>
  </section>
</body>
</html>
```